Signage Design Project

We are a company that sells roses at university and college graduations. We are looking for a sign for conferences. The sign will be a long lengthwise sign, 33.5w x 80xh
It doesn't need to be overwhelmingly flashy, it just needs to get our message across. We will require two signs, one with the "Marlowe Blooms" logo, and a second with the "Fenwick Petal Co." logo. These logos are uploaded in both PNG and JPEG formats. The alternative option is to create one image with both logos, but we would much prefer two separate ones. We will NOT look at anything overly flashy. Ideally we need a simple, aesthetically pleasing graphic that will look good on a vertical pop up stand.

Industry/Entity Type

University

Requirements
Must have
• Our logo (Marlowe Blooms for one, Fenwick Petal Co. for the other)

```html
<!DOCTYPE html>
<html lang="en">
<head>
<meta charset="utf-8">
<title>Marlowe Blooms – Vertical Banner</title>
<link rel="stylesheet" href="https://fonts.googleapis.com/css2?family=PT+Sans:wght@700&family=Roboto:wght@300&display=swap">
<style>
  :root {
    --page-bg: #f2f2f2;
    --banner-bg: #ffffff;
    --rose-pink: #e8335e;
    --rose-pink-fade: rgba(240, 90, 125, 0);
    --leaf-green: #17a355;
    --mint: #a6dfc0;
    --mint-fade: rgba(166, 223, 192, 0);
    --tagline-grey: #555555;
    --frame-line: #d9d9e3;
  }
  html, body {
    margin: 0;
    width: 1200px;
    height: 1000px;
    overflow: hidden;
    background: var(--page-bg);
  }
  .stage {
    position: relative;
    width: 1200px;
    height: 1000px;
  }
  .banner {
    position: absolute;
    left: 410px;
    top: 45px;
    width: 381px;
    height: 910px;
    background: var(--banner-bg);
    box-shadow: 0 0 0 1px var(--frame-line);
    overflow: hidden;
  }
  .corner-accent {
    position: absolute;
    top: 0;
    right: 0;
    width: 215px;
    height: 145px;
    background: radial-gradient(ellipse 100% 100% at 100% 0%, var(--rose-pink) 0%, rgba(240, 90, 125, 0.55) 55%, var(--rose-pink-fade) 100%);
  }
  .base-accent {
    position: absolute;
    left: 0;
    right: 0;
    bottom: 0;
    height: 135px;
    background: linear-gradient(to bottom, var(--mint-fade) 0%, rgba(166, 223, 192, 0.45) 45%, rgba(166, 223, 192, 0.25) 100%);
  }
  .brand {
    position: absolute;
    left: 0;
    right: 0;
    top: 262px;
    text-align: center;
  }
  .brand__dot {
    display: block;
    width: 96px;
    height: 96px;
    margin: 0 auto 22px;
    border-radius: 50%;
    background: var(--rose-pink);
  }
  .brand__name {
    margin: 0;
    font-family: "PT Sans", sans-serif;
    font-weight: 700;
    font-size: 46px;
    line-height: 1.05;
    color: var(--leaf-green);
    letter-spacing: -0.5px;
  }
  .tagline {
    position: absolute;
    left: 0;
    right: 0;
    top: 872px;
    margin: 0;
    text-align: center;
    font-family: "Roboto", sans-serif;
    font-weight: 300;
    font-size: 16px;
    letter-spacing: 1.6px;
    color: var(--tagline-grey);
  }
</style>
</head>
<body>
  <main class="stage">
    <section class="banner">
      <div class="corner-accent" role="img" aria-label="Soft pink petal-toned accent in the top right corner"></div>
      <div class="base-accent" role="img" aria-label="Soft mint-green wave accent along the bottom edge"></div>

      <div class="brand">
        <span class="brand__dot"></span>
        <h1 class="brand__name">Marlowe Blooms</h1>
      </div>

      <p class="tagline">Flowers for your graduate</p>
    </section>
  </main>
</body>
</html>
```